I have a small construction company that is growing. I specialize in commercial concrete and custom

I want a site that shows what we do. We specialize in custom deck design and builds. Custom home builds. Commercial concrete . project management

Target Market(s)

Commercial construction companies and custom home builders

Industry/Entity Type

Construction

Number of Pages Required

1 page

Font styles to use
Serif

Colors

Designer to choose colors to be used in the design.

Requirements
Must have
• Pictures and videos of project that we have completed or are in progress

```html
<!DOCTYPE html>
<html lang="en">
<head>
<meta charset="utf-8">
<title>Ridgeway Construction</title>
<link href="https://fonts.googleapis.com/css2?family=Roboto+Slab:wght@400;500;700&family=Source+Serif+4:ital,wght@0,400;0,600;1,400&display=swap" rel="stylesheet">
<style>
:root{
  --red:#e8393f;
  --red-deep:#d8262e;
  --ink:#222;
  --text:#555;
  --muted:#777;
  --pale:#f4f5f7;
  --line:#dcdcdc;
  --white:#fff;
  --head:'Roboto Slab',Georgia,serif;
  --body:'Source Serif 4',Georgia,serif;
}
*{box-sizing:border-box;margin:0;padding:0}
html,body{width:1200px;height:2469px;overflow:hidden}
body{position:relative;background:var(--white);font-family:var(--body);color:var(--ink)}
.abs{position:absolute}
.ctr{text-align:center;left:0;width:1200px}

/* header */
.brand{left:0;top:21px;width:197px;height:40px;background:var(--red);clip-path:polygon(0 0,100% 0,84% 100%,0 100%);color:var(--white);font-family:var(--head);font-size:24px;font-weight:500;line-height:40px;padding-left:30px}
.nav{top:33px;left:404px;display:flex;gap:40px;font-family:var(--head);font-size:14px;color:var(--ink)}
.phone{top:22px;right:54px;font-family:var(--head);font-size:13px;color:var(--ink)}
.quote-btn{left:1009px;top:51px;width:153px;height:31px;border-radius:16px;background:var(--red);color:var(--white);font-family:var(--head);font-size:13px;font-weight:500;text-align:center;line-height:31px}

/* hero */
.hero{left:0;top:0;width:1200px;height:543px;overflow:hidden;background:linear-gradient(90deg,#f3f2f0,#fbfbfa 55%,#fff)}
.hero-room{left:0;top:100px;width:620px;height:443px;background:linear-gradient(180deg,#f6f5f3,#efeeec);opacity:.8}
.hero-arc{left:556px;top:150px;width:760px;height:760px;border-radius:50%;background:var(--red)}
.hero-house{left:675px;top:145px;width:485px;height:370px;border-radius:8px;background:linear-gradient(160deg,#3a2f26 0%,#d9a94c 40%,#c98e34 70%,#e7e4e0 100%)}
.tagline{top:556px;font-size:21px;line-height:27px;color:var(--ink)}
.sub{top:618px;font-size:13px;color:var(--text)}
.project-btn{left:510px;top:657px;width:180px;height:35px;border:1.5px solid var(--red);border-radius:18px;color:var(--red);font-family:var(--head);font-size:12.5px;font-weight:700;display:flex;align-items:center;justify-content:center;gap:8px}

/* section heading */
.heading{font-family:var(--head);font-size:22px;font-weight:700}
.heading span{color:var(--red)}
.dots{left:53px;width:1094px;height:1.5px;background:repeating-linear-gradient(90deg,var(--red) 0 3px,transparent 3px 6px)}
.vdots{width:1.5px;background:repeating-linear-gradient(180deg,var(--red) 0 3px,transparent 3px 6px)}

/* services */
.services{left:0;top:711px;width:1200px;height:356px;background:var(--pale)}
.card{top:843px;width:253px;height:168px}
.card-photo{left:0;top:0;width:253px;height:125px}
.card-label{left:0;top:125px;width:253px;height:43px;background:linear-gradient(90deg,var(--red-deep),#f0676b);border-radius:0 0 26px 0;color:var(--white);font-family:var(--head);font-size:13.5px;text-align:center;line-height:43px}
.card-icon{left:103px;top:-25px;width:46px;height:46px;border-radius:50%;background:var(--red);border:3px solid var(--white);display:flex;align-items:center;justify-content:center}

/* projects */
.grid{left:0;top:1147px;width:1200px;display:grid;grid-template-columns:repeat(5,240px);grid-template-rows:178px 185px;gap:3px 0}
.tile{position:relative}
.play{position:absolute;left:96px;top:65px;width:48px;height:48px;border-radius:50%;background:rgba(232,57,63,.92);border:2px solid var(--white);display:flex;align-items:center;justify-content:center}

/* testimonials */
.voices{left:0;top:1542px;width:1200px;height:405px;background:linear-gradient(180deg,#eef0f2,#f5f5f6)}
.quote{width:406px;font-size:12.5px;line-height:18px;font-style:italic;color:var(--text)}
.quote.left{text-align:right}
.who{font-size:13px;color:var(--ink)}
.avatar{width:78px;height:78px;border-radius:50%;background:linear-gradient(160deg,#d8d2cc,#9c8e84);border:3px solid var(--white)}

/* contact */
.col-title{font-family:var(--head);font-size:17px;font-weight:700}
.field{left:53px;height:32px;border:1px solid #cfcfcf;border-radius:5px;font-size:12px;color:var(--muted);padding:8px 12px;background:var(--white)}
.send{left:53px;top:2227px;width:138px;height:31px;border-radius:16px;background:var(--red);color:var(--white);font-family:var(--head);font-size:12px;font-weight:700;text-align:center;line-height:31px}
.map{left:333px;top:2034px;width:534px;height:224px;background:linear-gradient(135deg,#cfe6c9,#a9cfe8 45%,#e9e6df 80%)}
.info{left:895px;width:260px;font-size:12.5px;line-height:20px;color:var(--text)}
.social{top:2228px;width:28px;height:28px;border-radius:50%;background:var(--red)}

/* footer */
.rule-red{left:0;width:1200px;background:var(--red)}
.foot-brand{left:1021px;top:2331px;width:179px;height:36px;background:var(--red);clip-path:polygon(14% 0,100% 0,100% 100%,0 100%,0 0);color:var(--white);font-family:var(--head);font-size:21px;font-weight:500;line-height:36px;padding-left:50px}
.foot-nav{left:90px;top:2353px;display:flex;gap:24px;font-family:var(--head);font-size:13px;font-weight:700}
.foot-links{left:53px;top:2396px;display:flex;gap:20px;font-size:11px;color:var(--text)}
.foot-legal{right:53px;top:2396px;display:flex;gap:20px;font-size:11px;color:var(--text)}
</style>
</head>
<body>

<!-- hero -->
<section class="abs hero">
  <div class="abs hero-room" role="img" aria-label="Faded photo of a bright interior room with a window"></div>
  <div class="abs hero-arc"></div>
  <div class="abs hero-house" role="img" aria-label="Illustration of a cut-away two-storey timber house with a wraparound deck"></div>
</section>

<header>
  <div class="abs brand">Ridgeway</div>
  <nav class="abs nav"><span>ABOUT US</span><span>SERVICE</span><span>GALLERY</span><span>CONTACT US</span></nav>
  <div class="abs phone">+1 (555) 014 22 80</div>
  <div class="abs quote-btn">Request a Quote</div>
</header>

<p class="abs ctr tagline">High quality craftsmanship and professional service on custom decks, custom homes<br>Specializing in Commercial Concrete and Project Management</p>
<p class="abs ctr sub">See some of the features below and learn why People trust Ridgeway Construction</p>
<div class="abs project-btn"><svg width="10" height="12" viewBox="0 0 10 12"><path d="M0 0L10 6L0 12Z" fill="#e8393f"/></svg>SEE OUR PROJECT</div>

<!-- services -->
<section class="abs services"></section>
<h2 class="abs ctr heading" style="top:727px">Our <span>Services</span></h2>
<div class="abs dots" style="top:767px"></div>

<div class="abs card" style="left:53px">
  <div class="abs card-photo" role="img" aria-label="Photo of a custom timber deck with railings" style="background:linear-gradient(180deg,#a9c3dc,#9a6e42)"></div>
  <div class="abs card-label">Custom Deck Design</div>
  <div class="abs card-icon"><svg width="20" height="20" viewBox="0 0 20 20"><rect x="2" y="4" width="16" height="3" fill="#fff"/><rect x="2" y="9" width="16" height="3" fill="#fff"/><rect x="2" y="14" width="16" height="3" fill="#fff"/></svg></div>
</div>
<div class="abs card" style="left:333px">
  <div class="abs card-photo" role="img" aria-label="Photo of a custom family home under construction" style="background:linear-gradient(180deg,#5d86c2,#8a7f6b)"></div>
  <div class="abs card-label">Custom Home Builds</div>
  <div class="abs card-icon"><svg width="20" height="20" viewBox="0 0 20 20"><path d="M2 9L10 3L18 9V17H2Z" fill="#fff"/></svg></div>
</div>
<div class="abs card" style="left:614px">
  <div class="abs card-photo" role="img" aria-label="Photo of a commercial concrete slab being poured" style="background:linear-gradient(180deg,#b9b6ae,#7f7b73)"></div>
  <div class="abs card-label">Commercial Concrete</div>
  <div class="abs card-icon"><svg width="20" height="20" viewBox="0 0 20 20"><rect x="2" y="11" width="16" height="6" fill="#fff"/><rect x="5" y="4" width="10" height="5" fill="#fff"/></svg></div>
</div>
<div class="abs card" style="left:895px">
  <div class="abs card-photo" role="img" aria-label="Photo of engineers in hard hats on a building site" style="background:linear-gradient(180deg,#3f6fb5,#c98a3f)"></div>
  <div class="abs card-label">Project Management</div>
  <div class="abs card-icon"><svg width="20" height="20" viewBox="0 0 20 20"><circle cx="10" cy="7" r="4" fill="#fff"/><path d="M3 18C3 13 17 13 17 18Z" fill="#fff"/></svg></div>
</div>

<!-- projects -->
<h2 class="abs ctr heading" style="top:1082px">Latest <span>Projects</span></h2>
<div class="abs dots" style="top:1123px"></div>
<div class="abs grid">
  <div class="tile" role="img" aria-label="Modern house with lit deck at dusk" style="background:linear-gradient(180deg,#3c6fb0,#5a4a3a)"></div>
  <div class="tile" role="img" aria-label="Video of a contemporary villa build in progress" style="background:linear-gradient(180deg,#7a8aa6,#4d5b3a)"><span class="play"><svg width="16" height="18" viewBox="0 0 16 18"><path d="M2 1L15 9L2 17Z" fill="#fff"/></svg></span></div>
  <div class="tile" role="img" aria-label="Two-storey stone house with lit entrance" style="background:linear-gradient(180deg,#8d99ad,#6b6459)"></div>
  <div class="tile" role="img" aria-label="Warm wood-panelled living room" style="background:linear-gradient(180deg,#b7834c,#6e4a2c)"></div>
  <div class="tile" role="img" aria-label="Single-storey custom home with garden" style="background:linear-gradient(180deg,#5270a4,#6d8a54)"></div>
  <div class="tile" role="img" aria-label="Country house with concrete driveway" style="background:linear-gradient(180deg,#a7c0dc,#5f8a3e)"></div>
  <div class="tile" role="img" aria-label="Video of a log cabin build in snowy mountains" style="background:linear-gradient(180deg,#4a5f9a,#d7dde8)"><span class="play"><svg width="16" height="18" viewBox="0 0 16 18"><path d="M2 1L15 9L2 17Z" fill="#fff"/></svg></span></div>
  <div class="tile" role="img" aria-label="Cream villa among trees" style="background:linear-gradient(180deg,#6ca1d6,#4f8f3a)"></div>
  <div class="tile" role="img" aria-label="Stone and timber house with covered deck" style="background:linear-gradient(180deg,#4d87c9,#3f7a2c)"></div>
  <div class="tile" role="img" aria-label="Video of a brick house and pool deck in progress" style="background:linear-gradient(180deg,#9fb1c7,#5a7a96)"><span class="play"><svg width="16" height="18" viewBox="0 0 16 18"><path d="M2 1L15 9L2 17Z" fill="#fff"/></svg></span></div>
</div>

<!-- testimonials -->
<section class="abs voices" role="img" aria-label="Faded photo of a bright living room behind the testimonials"></section>
<h2 class="abs ctr heading" style="top:1573px">What <span>People Say</span></h2>
<div class="abs dots" style="top:1613px"></div>
<div class="abs vdots" style="left:600px;top:1646px;height:232px"></div>
<div class="abs dots" style="top:1770px"></div>

<p class="abs quote left" style="left:58px;top:1660px">Duis aute irure dolor in reprehenderit in voluptate velit esse cillum dolore eu fugiat nulla pariatur. Excepteur sint occaecat cupidatat non proident, sunt in culpa qui officia deserunt mollit.</p>
<p class="abs who" style="right:738px;top:1728px">Owen Marsh, Operations Manager</p>
<div class="abs avatar" role="img" aria-label="Portrait of Owen Marsh" style="left:489px;top:1656px"></div>

<div class="abs avatar" role="img" aria-label="Portrait of Clara Voss" style="left:633px;top:1656px"></div>
<p class="abs quote" style="left:739px;top:1660px">Provident, similique sunt in culpa qui officia deserunt mollitia animi, id est laborum et dolorum fuga. Et harum quidem rerum facilis est et expedita distinctio. Nam libero tempore, cum soluta nobis.</p>
<p class="abs who" style="left:739px;top:1728px">Clara Voss, Creative Designer</p>

<p class="abs quote left" style="left:58px;top:1797px">Luis aute irure dolor in reprehenderit in piluptate velit esse cillum dolore eu fugiat nulla pariatur. Excepteur sint occaecat cupidatat non proident, sunt in culpa qui officia deserunt mollit.</p>
<p class="abs who" style="right:738px;top:1866px">Nina Hale, Manager</p>
<div class="abs avatar" role="img" aria-label="Portrait of Nina Hale" style="left:489px;top:1796px"></div>

<div class="abs avatar" role="img" aria-label="Portrait of Paul Brandt" style="left:633px;top:1796px"></div>
<p class="abs quote" style="left:739px;top:1797px">At vero eos et accusamus et iusto odio dignissimos ducimus qui blanditiis praesentium voluptatum deleniti atque corrupti quos dolores et quas molestias excepturi sint occaecati asperiores.</p>
<p class="abs who" style="left:739px;top:1866px">Paul Brandt, Developer</p>

<!-- contact -->
<h3 class="abs col-title" style="left:53px;top:1987px">Feel Free to Mail</h3>
<div class="abs field" style="top:2034px;width:115px">Name *</div>
<div class="abs field" style="left:189px;top:2034px;width:116px">Email *</div>
<div class="abs field" style="top:2086px;width:252px">Subject</div>
<div class="abs field" style="top:2137px;width:252px;height:69px">Write Your Message Here...</div>
<div class="abs send">SEND MESSAGE</div>

<h3 class="abs col-title" style="left:333px;width:534px;text-align:center;top:1992px">Headquarters</h3>
<div class="abs map" role="img" aria-label="Street map showing the headquarters location"></div>
<svg class="abs" style="left:588px;top:2126px" width="24" height="34" viewBox="0 0 24 34"><path d="M12 0C5 0 0 5 0 12C0 21 12 34 12 34S24 21 24 12C24 5 19 0 12 0Z" fill="#e8393f"/><circle cx="12" cy="12" r="4" fill="#a11"/></svg>

<h3 class="abs col-title" style="left:895px;top:1987px">Contact Info</h3>
<p class="abs info" style="top:2028px">Our staff is available to you from 9AM until 5PM on weekdays.</p>
<p class="abs info" style="top:2080px">Phone: +1 (555) 014 69 31</p>
<p class="abs info" style="top:2114px">Office: Harborline Plaza, Suite 4</p>
<p class="abs info" style="top:2148px">Email: hello@ridgewaybuild.com</p>
<h3 class="abs col-title" style="left:895px;top:2183px">Follow Us on</h3>
<div class="abs social" style="left:895px"></div>
<div class="abs social" style="left:933px"></div>
<div class="abs social" style="left:971px"></div>
<div class="abs social" style="left:1009px"></div>
<div class="abs social" style="left:1047px"></div>

<!-- footer -->
<div class="abs rule-red" style="top:2308px;height:2px"></div>
<div class="abs foot-brand">Ridgeway</div>
<svg class="abs" style="left:50px;top:2353px" width="14" height="14" viewBox="0 0 14 14"><circle cx="6" cy="6" r="4.5" fill="none" stroke="#777" stroke-width="1.6"/><path d="M9.5 9.5L13 13" stroke="#777" stroke-width="1.6"/></svg>
<nav class="abs foot-nav"><span>Help &amp; Contact</span><span>Services</span><span>Gallery</span><span>Request a Quote</span></nav>
<div class="abs" style="left:53px;top:2382px;width:1094px;border-top:1px solid var(--line)"></div>
<nav class="abs foot-links"><span>About</span><span>Careers</span><span>Public Policy</span><span>Sitemap</span><span>People</span><span>Partners</span></nav>
<nav class="abs foot-legal"><span>© 2006 - 2018</span><span>Privacy</span><span>Legal</span><span>Feedback</span></nav>
<div class="abs rule-red" style="top:2464px;height:5px"></div>

</body>
</html>
```